Data Compass Plan- Brennal Insurance providing specialist Cyber and Liability Insurance

for Managed Technology Service Providers and their customer, we will use a letterhead that white labels insurer documents, which can be used in our physical letters as well as to be used within Email signatures.

Target Market(s)

Managed Technology Services Providers

Industry/Entity Type

Cyber Insurance

Requirements
Must have
• website, email address, contact phone numbers

```html
<!DOCTYPE html>
<html lang="en">
<head>
<meta charset="utf-8">
<title>Data Compass Plan – Letterhead</title>
<link rel="stylesheet" href="https://fonts.googleapis.com/css2?family=Montserrat:wght@600&family=Open+Sans:wght@400;600&display=swap">
<style>
  :root {
    --backdrop: #b9b9b9;
    --paper: #ffffff;
    --ink: #3d3d3d;
    --ink-soft: #555555;
    --accent: #3fae3f;
    --signature-tone: #e6e6e6;
  }
  * { box-sizing: border-box; margin: 0; padding: 0; }
  html, body { width: 1200px; height: 800px; overflow: hidden; }
  body {
    background: var(--backdrop);
    font-family: "Open Sans", Arial, sans-serif;
    color: var(--ink);
    display: flex;
    justify-content: center;
    align-items: center;
    gap: 44px;
  }
  .sheet {
    position: relative;
    width: 509px;
    height: 720px;
    background: var(--paper);
    box-shadow: 0 6px 18px rgba(0,0,0,0.18);
  }
  .brand {
    position: absolute;
    top: 52px;
    right: 44px;
    display: flex;
    align-items: center;
    gap: 10px;
    font-family: "Montserrat", Arial, sans-serif;
    font-weight: 600;
    font-size: 30px;
    letter-spacing: 0.5px;
    color: var(--ink);
  }
  .brand-mark {
    width: 14px;
    height: 14px;
    background: var(--accent);
  }
  .letter {
    position: absolute;
    top: 130px;
    left: 70px;
    width: 360px;
  }
  .greeting {
    color: var(--accent);
    font-size: 9px;
    margin-bottom: 12px;
  }
  .body-text p {
    font-size: 7px;
    line-height: 1.4;
    color: var(--ink-soft);
    margin-bottom: 9px;
    text-indent: 24px;
  }
  .sign-off {
    margin-top: 14px;
    font-size: 7px;
    color: var(--ink-soft);
  }
  .signature {
    width: 70px;
    height: 14px;
    margin: 5px 0;
    background: var(--signature-tone);
  }
  .signer { text-transform: uppercase; }
  .contact {
    position: absolute;
    left: 48px;
    bottom: 150px;
    list-style: none;
    font-size: 11px;
    line-height: 1.5;
    color: var(--ink);
  }
  .contact li { display: flex; align-items: center; gap: 6px; }
  .contact svg { width: 9px; height: 9px; fill: var(--accent); flex: none; }
  .address {
    position: absolute;
    right: 60px;
    bottom: 46px;
    font-size: 11px;
    line-height: 1.45;
    text-align: right;
    font-style: normal;
    color: var(--ink);
  }
</style>
</head>
<body>

<section class="sheet sheet--letter">
  <div class="brand"><span class="brand-mark"></span>Data Compass Plan</div>

  <div class="letter">
    <p class="greeting">Dear Mr. Ellery</p>
    <div class="body-text">
      <p>Lorem Ipsum is simply dummy text of the printing and typesetting industry. Lorem Ipsum has been the industry's standard dummy text ever since the 1500s, when an unknown printer took a galley of type and scrambled it to make a type specimen book. It has survived not only five centuries, but also the leap into electronic typesetting, remaining essentially unchanged. It was popularised in the 1960s with the release of Letraset sheets containing Lorem Ipsum passages</p>
      <p>Lorem Ipsum is simply dummy text of the printing and typesetting industry. Lorem Ipsum has been the industry's standard dummy text ever since the 1500s, when an unknown printer took a galley of type and scrambled it to make a type specimen book. It has survived not only five centuries, but also the leap into electronic typesetting, remaining essentially unchanged. It was popularised in the 1960s with the release of Letraset sheets containing Lorem Ipsum passages</p>
      <p>Lorem Ipsum is simply dummy text of the printing and typesetting industry. Lorem Ipsum has been the industry's standard dummy text ever since the 1500s, when an unknown printer took a galley of type and scrambled it to make a type specimen book. It has survived not only five centuries, but also the leap into electronic typesetting, remaining essentially unchanged. It was popularised in the 1960s with the release of Letraset sheets containing Lorem Ipsum passages</p>
      <p>Lorem Ipsum is simply dummy text of the printing and typesetting industry. Lorem Ipsum has been the industry's standard dummy text ever since the 1500s, when an unknown printer took a galley of type and scrambled it to make a type specimen book. It has survived not only five centuries, but also the leap into electronic typesetting, remaining essentially unchanged. It was popularised in the 1960s with the release of Letraset sheets containing Lorem Ipsum passages</p>
      <p>Lorem Ipsum is simply dummy text of the printing and typesetting industry. Lorem Ipsum has been the industry's standard dummy text ever since the 1500s, when an unknown printer took a galley of type and scrambled it to make a type specimen book. It has survived not only five centuries, but also the leap into electronic typesetting, remaining essentially unchanged. It was popularised in the 1960s with the release of Letraset sheets containing Lorem Ipsum passages</p>
    </div>
    <div class="sign-off">
      <p>Sincerely</p>
      <div class="signature" role="img" aria-label="Handwritten signature"></div>
      <p class="signer">Alan Pryce</p>
    </div>
  </div>

  <ul class="contact">
    <li><svg viewBox="0 0 10 10"><path d="M2 0.5 L4 2.8 L3 4 Q4 6 6 7 L7.2 6 L9.5 8 L8 9.6 Q3.5 9.5 0.4 2 Z"/></svg>555 014 288</li>
    <li><svg viewBox="0 0 10 10"><path d="M0.5 2 H9.5 V8 H0.5 Z M0.5 2 L5 5.5 L9.5 2" stroke="#fff" stroke-width="0.8"/></svg>info@datacompassplan.com</li>
    <li><svg viewBox="0 0 10 10"><circle cx="5" cy="5" r="4.5"/></svg>www.datacompassplan.com</li>
  </ul>

  <address class="address">1180 Larkfield Quay<br>Marlow Bay CA 90417</address>
</section>

<section class="sheet sheet--blank">
  <div class="brand"><span class="brand-mark"></span>Data Compass Plan</div>

  <ul class="contact">
    <li><svg viewBox="0 0 10 10"><path d="M2 0.5 L4 2.8 L3 4 Q4 6 6 7 L7.2 6 L9.5 8 L8 9.6 Q3.5 9.5 0.4 2 Z"/></svg>555 014 288</li>
    <li><svg viewBox="0 0 10 10"><path d="M0.5 2 H9.5 V8 H0.5 Z M0.5 2 L5 5.5 L9.5 2" stroke="#fff" stroke-width="0.8"/></svg>info@datacompassplan.com</li>
    <li><svg viewBox="0 0 10 10"><circle cx="5" cy="5" r="4.5"/></svg>www.datacompassplan.com</li>
  </ul>

  <address class="address">1180 Larkfield Quay<br>Marlow Bay CA 90417</address>
</section>

</body>
</html>
```